Bramble Roofing Website Relaunch

We require a re-launch of our website, We are a longrun roofing company based in New Zealand, we are rapidly expanding and require a more professionally presented website our current website is www.brambleroofing.co.nz we want something modern, masculine and communicates a "strong" "superior" image, we already have a logo which I have attached we use the orange and silver one as you will see on our current website

Industry/Entity Type

It Company

Number of Pages Required

1 page

Colors
f37122
f78f20
000000
1b1b1b
474747
d3d3d3
f5f5f5

Requirements
Must have
• Images of our work
• Email and Mobile Contact Details
• Link to Facebook page
• Who We Are, What We Do
• Certified Trade Craftsman Logo
• Our Logo

```html
<!DOCTYPE html>
<html lang="en">
<head>
<meta charset="utf-8">
<title>Bramble Roofing</title>
<link href="https://fonts.googleapis.com/css2?family=Oswald:wght@500&family=Raleway:wght@700;800&family=Exo+2:wght@600&family=Lato:wght@400;700&display=swap" rel="stylesheet">
<style>
:root{
  --orange:#f37122;
  --orange-light:#f78f20;
  --black:#000000;
  --dark:#1b1b1b;
  --mid:#474747;
  --silver:#d3d3d3;
  --pale:#f5f5f5;
  --grey-band:#8a8a8a;
  --footer:#2b2b2b;
  --white:#ffffff;
}
*{box-sizing:border-box;margin:0;padding:0}
html,body{width:1200px;height:2848px;overflow:hidden}
body{font-family:'Lato',sans-serif;color:var(--mid);background:var(--white);position:relative}
.container{width:1002px;margin:0 auto;position:relative}

/* header */
.site-header{height:118px}
.site-header .container{display:flex;align-items:center;justify-content:space-between;height:118px}
.brand{display:flex;align-items:center;gap:14px}
.brand-mark{width:52px;height:52px;background:var(--orange)}
.brand-name{font-family:'Raleway',sans-serif;font-weight:800;font-size:30px;color:var(--mid);letter-spacing:1px;text-transform:uppercase}
.header-contacts{display:flex;gap:38px}
.contact-item{display:flex;align-items:center;gap:10px}
.contact-item svg{width:36px;height:36px}
.contact-label{font-size:15px;color:var(--orange);font-weight:700}
.contact-value{font-size:15px;color:var(--mid)}

/* nav */
.main-nav{height:44px;background:var(--grey-band);border-top:2px solid #a0a0a0}
.main-nav ul{list-style:none;display:flex;height:42px;width:1002px;margin:0 auto}
.main-nav li{flex:1;text-align:center;font-family:'Raleway',sans-serif;font-weight:800;font-size:15px;color:var(--white);line-height:42px;letter-spacing:1px}
.main-nav li.active{flex:0 0 150px;background:linear-gradient(var(--orange-light),var(--orange));border-bottom:3px solid #c85a18}

/* hero */
.hero{position:relative;height:512px;background:linear-gradient(180deg,#aec4d8 0%,#d8e2ea 35%,#596066 55%,#2a2c30 70%,#6f9a3e 76%,#5a8a2c 100%)}
.hero-title{position:absolute;left:0;right:0;top:420px;text-align:center;font-family:'Oswald',sans-serif;font-weight:500;font-size:41px;color:var(--white);text-shadow:0 2px 6px rgba(0,0,0,.5)}
.hero-arrow{position:absolute;top:206px;width:38px;height:38px;background:rgba(30,30,30,.85);display:flex;align-items:center;justify-content:center}
.hero-arrow.prev{left:4px}.hero-arrow.next{right:4px}

/* service bands */
.service-bands{display:flex;height:135px}
.band{flex:1;display:flex;align-items:center;padding-left:99px;gap:34px;color:var(--white)}
.band.residential{background:linear-gradient(90deg,#c4631f,var(--orange-light) 60%,#e48a3a)}
.band.commercial{background:var(--grey-band);padding-left:40px}
.band svg{width:104px;height:104px;flex:none}
.band h3{font-family:'Exo 2',sans-serif;font-weight:600;font-size:20px;letter-spacing:1px;margin-bottom:4px}
.band p{font-size:14px;line-height:21px;width:325px}

/* section titles */
.section-title{text-align:center;font-family:'Raleway',sans-serif;font-weight:800;font-size:30px;letter-spacing:1px;color:var(--mid)}
.section-title span{color:var(--orange)}
.divider{display:flex;justify-content:center;margin:6px 0 0}

.btn{display:inline-block;background:linear-gradient(var(--orange-light),var(--orange));color:var(--white);font-family:'Raleway',sans-serif;font-weight:800;font-size:13px;letter-spacing:1px;padding:0 16px;height:36px;line-height:36px;box-shadow:0 2px 3px rgba(0,0,0,.25)}

/* who we are */
.who-we-are{height:315px;text-align:center;padding-top:45px}
.who-we-are p{font-size:14px;line-height:27px;color:var(--mid);margin:25px auto 26px;width:1002px}

/* what we do */
.what-we-do{height:823px;position:relative;background:linear-gradient(180deg,#2a3038 0%,#1f242b 50%,#171a1f 100%);padding-top:44px;color:var(--white)}
.what-we-do .section-title{color:var(--white)}
.what-we-do .intro{text-align:center;font-size:14px;margin-top:26px;color:#e6e6e6}
.service-grid{display:grid;grid-template-columns:repeat(3,315px);column-gap:28px;margin-top:36px}
.service-card{text-align:center;height:306px}
.service-photo{height:184px;border:2px solid #d3d3d3}
.service-card h4{font-family:'Exo 2',sans-serif;font-weight:600;font-size:18px;margin-top:17px;letter-spacing:.5px}
.plus{display:inline-flex;width:23px;height:23px;background:var(--orange);align-items:center;justify-content:center;margin-top:16px}

/* our work */
.our-work{height:573px;background:linear-gradient(180deg,#e4edf3 0%,#f5f5f5 40%,#e8e8e8 100%);padding-top:40px;text-align:center}
.work-grid{display:grid;grid-template-columns:repeat(4,239px);gap:18px 15px;margin-top:38px}
.work-tile{height:158px;border:1px solid #b8b8b8;position:relative}
.work-tile.highlight{background:#3c3e42;display:flex;flex-direction:column;align-items:center;justify-content:center;color:var(--white);font-size:14px;line-height:20px}
.work-tile.highlight svg{margin-bottom:10px}
.our-work .btn{margin-top:26px}

/* footer */
.site-footer{height:285px;background:var(--footer);color:#d8d8d8;padding-top:40px}
.footer-cols{display:flex}
.footer-col h5{font-family:'Raleway',sans-serif;font-weight:800;font-size:15px;color:var(--white);letter-spacing:1px}
.footer-col .rule{width:30px;height:2px;background:var(--silver);margin:10px 0 18px}
.quick-links{width:216px}
.quick-links li{list-style:none;font-size:13px;line-height:30px}
.quick-links li::before{content:"›";margin-right:8px;color:var(--white)}
.contact-details{width:336px}
.contact-details .row{display:flex;gap:12px;font-size:13px;line-height:17px;margin-bottom:13px}
.contact-details strong{color:var(--white)}
.contact-details svg{width:14px;height:14px;flex:none;margin-top:1px}
.location-map{width:352px}
.map-box{width:241px;height:143px;border:4px solid #6a6a6a;background:linear-gradient(135deg,#e6e2da,#d7d2c8)}
.cert-badge{width:98px;height:99px;background:var(--white);margin-top:66px;display:flex;align-items:center;justify-content:center}

.bottom-bar{position:absolute;left:0;right:0;bottom:0;height:43px;background:linear-gradient(90deg,#c4631f,var(--orange-light) 50%,#d96e28)}
.bottom-bar .container{display:flex;justify-content:space-between;align-items:center;height:43px;font-size:13px;color:var(--white)}
</style>
</head>
<body>

<header class="site-header">
  <div class="container">
    <div class="brand">
      <div class="brand-mark"></div>
      <div class="brand-name">Bramble Roofing</div>
    </div>
    <div class="header-contacts">
      <div class="contact-item">
        <svg viewBox="0 0 36 36"><path d="M10 6c-3 2-5 5-3 10 3 7 8 12 14 14 4 1 7-1 8-3l-5-5-3 3c-3-1-6-4-7-7l3-3z" fill="none" stroke="#f37122" stroke-width="2.5" stroke-linejoin="round"/></svg>
        <div><div class="contact-label">Call Us:</div><div class="contact-value">021 555 01234</div></div>
      </div>
      <div class="contact-item">
        <svg viewBox="0 0 36 36"><rect x="4" y="9" width="28" height="19" fill="none" stroke="#f37122" stroke-width="2.5"/><path d="M4 9l14 11 14-11" fill="none" stroke="#f37122" stroke-width="2.5"/></svg>
        <div><div class="contact-label">Mail Us:</div><div class="contact-value">hello@brambleroofing.co.nz</div></div>
      </div>
    </div>
  </div>
</header>

<nav class="main-nav">
  <ul>
    <li class="active">HOME</li>
    <li>WHO WE ARE</li>
    <li>WHAT WE DO</li>
    <li>OUR WORK</li>
    <li>CONTACT US</li>
  </ul>
</nav>

<section class="hero" role="img" aria-label="Dark weatherboard house with a new long run roof on a green lawn under a cloudy sky">
  <div class="hero-arrow prev"><svg width="14" height="14" viewBox="0 0 14 14"><path d="M10 1L3 7l7 6z" fill="#fff"/></svg></div>
  <div class="hero-arrow next"><svg width="14" height="14" viewBox="0 0 14 14"><path d="M4 1l7 6-7 6z" fill="#fff"/></svg></div>
  <h1 class="hero-title">LONG RUN ROOFING SPECIALISTS</h1>
</section>

<section class="service-bands">
  <div class="band residential">
    <svg viewBox="0 0 104 104"><rect x="22" y="22" width="60" height="60" transform="rotate(45 52 52)" fill="none" stroke="#fff" stroke-width="4"/><path d="M36 54l16-14 16 14M40 51v16h24V51" fill="none" stroke="#fff" stroke-width="3"/><rect x="48" y="58" width="8" height="9" fill="#fff"/></svg>
    <div>
      <h3>RESIDENTIAL</h3>
      <p>Lorem ipsum dolor sit amet, consectetuer adipiscing elit, sed diam nonummy nibh euismod tincidunt ut laoreet dolore magna aliquam erat...<strong>[+]</strong></p>
    </div>
  </div>
  <div class="band commercial">
    <svg viewBox="0 0 104 104"><rect x="22" y="22" width="60" height="60" transform="rotate(45 52 52)" fill="none" stroke="#fff" stroke-width="4"/><rect x="40" y="38" width="24" height="30" fill="#fff"/><g fill="#8a8a8a"><rect x="44" y="42" width="4" height="4"/><rect x="50" y="42" width="4" height="4"/><rect x="56" y="42" width="4" height="4"/><rect x="44" y="50" width="4" height="4"/><rect x="50" y="50" width="4" height="4"/><rect x="56" y="50" width="4" height="4"/><rect x="49" y="59" width="6" height="9"/></g></svg>
    <div>
      <h3>COMMERCIAL</h3>
      <p>Lorem ipsum dolor sit amet, consectetuer adipiscing elit, sed diam nonummy nibh euismod tincidunt ut laoreet dolore magna aliquam erat...<strong>[+]</strong></p>
    </div>
  </div>
</section>

<section class="who-we-are">
  <h2 class="section-title">WHO <span>WE ARE</span></h2>
  <div class="divider"><svg width="110" height="18" viewBox="0 0 110 18"><path d="M0 9h44M66 9h44" stroke="#b0b0b0" stroke-width="1"/><rect x="49" y="3" width="12" height="12" transform="rotate(45 55 9)" fill="none" stroke="#f37122" stroke-width="1.5"/><rect x="52" y="6" width="6" height="6" transform="rotate(45 55 9)" fill="#f37122"/></svg></div>
  <p>We are a local, family owned and operated company with over 18 years extensive experience in the roofing industry, Roofing not only Waikato and Auckland but surrounding areas also. We are committed to providing superior service to our customers regardless of how big or small your project is, Your satisfaction is our guarantee. We take pride in installing quality products, Offering a workmanship guarantee and manufacturers material warranties where applicable.</p>
  <span class="btn">READ MORE</span>
</section>

<section class="what-we-do" role="img" aria-label="Roofer working on a tiled roof, darkened background">
  <div class="container">
    <h2 class="section-title">WHAT WE DO</h2>
    <div class="divider"><svg width="110" height="18" viewBox="0 0 110 18"><path d="M0 9h44M66 9h44" stroke="#777" stroke-width="1"/><rect x="49" y="3" width="12" height="12" transform="rotate(45 55 9)" fill="none" stroke="#f37122" stroke-width="1.5"/><rect x="52" y="6" width="6" height="6" transform="rotate(45 55 9)" fill="#f37122"/></svg></div>
    <p class="intro">At Bramble Roofing we offer a variety of professional services specializing in Residential, Industrial and Commercial Long Run Roofing Installations</p>
    <div class="service-grid">
      <div class="service-card"><div class="service-photo" role="img" aria-label="House with a new metal roof" style="background:linear-gradient(#8fb0d0,#c9d6df 45%,#9aa3a8 60%,#6b8a4a)"></div><h4>New Roofs And Re-Roofs</h4><span class="plus"><svg width="11" height="11"><path d="M5.5 0v11M0 5.5h11" stroke="#fff" stroke-width="2"/></svg></span></div>
      <div class="service-card"><div class="service-photo" role="img" aria-label="Building with dark metal cladding" style="background:linear-gradient(#c8ccd0,#3a3d40 30%,#2a2c2e 80%,#5b6b4a)"></div><h4>Metal Cladding</h4><span class="plus"><svg width="11" height="11"><path d="M5.5 0v11M0 5.5h11" stroke="#fff" stroke-width="2"/></svg></span></div>
      <div class="service-card"><div class="service-photo" role="img" aria-label="Dark metal fascia and spouting on a building" style="background:linear-gradient(90deg,#2e3133,#3d4144 60%,#7e8f6a)"></div><h4>Spouting and Metal Fascia</h4><span class="plus"><svg width="11" height="11"><path d="M5.5 0v11M0 5.5h11" stroke="#fff" stroke-width="2"/></svg></span></div>
      <div class="service-card"><div class="service-photo" role="img" aria-label="Large green clad shed with down pipes" style="background:linear-gradient(#b7c3cc,#4d5a4b 35%,#3e4a3c 80%,#7a7f73)"></div><h4>Down Pipes</h4><span class="plus"><svg width="11" height="11"><path d="M5.5 0v11M0 5.5h11" stroke="#fff" stroke-width="2"/></svg></span></div>
      <div class="service-card"><div class="service-photo" role="img" aria-label="House under alteration with new roof framing" style="background:linear-gradient(#c6d0d8,#9ea6ab 45%,#5e6360 70%,#4b5a3e)"></div><h4>Alterations</h4><span class="plus"><svg width="11" height="11"><path d="M5.5 0v11M0 5.5h11" stroke="#fff" stroke-width="2"/></svg></span></div>
      <div class="service-card"><div class="service-photo" role="img" aria-label="Metal roof extension seen from above" style="background:linear-gradient(135deg,#8a9096,#3c4044 50%,#6c7074)"></div><h4>Extensions</h4><span class="plus"><svg width="11" height="11"><path d="M5.5 0v11M0 5.5h11" stroke="#fff" stroke-width="2"/></svg></span></div>
    </div>
  </div>
</section>

<section class="our-work">
  <div class="container">
    <h2 class="section-title">OUR <span>WORK</span></h2>
    <div class="divider"><svg width="110" height="18" viewBox="0 0 110 18"><path d="M0 9h44M66 9h44" stroke="#b0b0b0" stroke-width="1"/><rect x="49" y="3" width="12" height="12" transform="rotate(45 55 9)" fill="none" stroke="#f37122" stroke-width="1.5"/><rect x="52" y="6" width="6" height="6" transform="rotate(45 55 9)" fill="#f37122"/></svg></div>
    <div class="work-grid">
      <div class="work-tile" role="img" aria-label="House with new dark roof under construction" style="background:linear-gradient(#9fb4c6,#c5ccd0 40%,#5a5e60 70%,#7b7a6e)"></div>
      <div class="work-tile" role="img" aria-label="Large curved roof on a commercial building" style="background:linear-gradient(#b8c4ce,#d4d8da 45%,#8a9094 65%,#5d6a4c)"></div>
      <div class="work-tile highlight">
        <svg width="30" height="30" viewBox="0 0 30 30"><circle cx="15" cy="15" r="13" fill="none" stroke="#fff" stroke-width="1.5"/><path d="M15 9v12M9 15h12" stroke="#fff" stroke-width="1.5"/></svg>
        Lorem ipsum dolor sit amet,<br>consectetuer adipiscing.
      </div>
      <div class="work-tile" role="img" aria-label="Long run roof ridge from above" style="background:linear-gradient(#c0c8ce,#8d9398 30%,#2f3336 55%,#4a4e50)"></div>
      <div class="work-tile" role="img" aria-label="Two storey house clad with scaffolding" style="background:linear-gradient(#9fb6c8,#bfc6c8 40%,#7c7f78 75%,#6a7b52)"></div>
      <div class="work-tile" role="img" aria-label="New home with roofing installed" style="background:linear-gradient(#b6c2cc,#cfcfcb 45%,#6e6f6a 75%,#5b6a48)"></div>
      <div class="work-tile" role="img" aria-label="Blue roof structure against clear sky" style="background:linear-gradient(#6f93c0,#9fb8d4 40%,#3b5b8a 70%,#6a6c62)"></div>
      <div class="work-tile" role="img" aria-label="Open shed with metal roof" style="background:linear-gradient(#c9cfd4,#7a7470 40%,#4a3f36 80%,#8a7a62)"></div>
    </div>
    <span class="btn">VIEW ALL</span>
  </div>
</section>

<footer class="site-footer">
  <div class="container footer-cols">
    <div class="footer-col quick-links">
      <h5>QUICK LINKS</h5><div class="rule"></div>
      <ul><li>Home</li><li>Who We Are</li><li>What We Do</li><li>Our Work</li><li>Contact Us</li></ul>
    </div>
    <div class="footer-col contact-details">
      <h5>CONTACT DETAILS</h5><div class="rule"></div>
      <div class="row"><svg viewBox="0 0 14 14"><path d="M7 1a4 4 0 0 0-4 4c0 3 4 8 4 8s4-5 4-8a4 4 0 0 0-4-4z" fill="#fff"/><circle cx="7" cy="5" r="1.5" fill="#2b2b2b"/></svg><div><strong>Bramble Roofing Ltd</strong><br>Fernhill, Ashvale, New Zealand</div></div>
      <div class="row"><svg viewBox="0 0 14 14"><path d="M3 1c-1.5 1-2 3-1 5 1.5 3 4 5.5 6.5 6.5 2 .8 3.5 0 4-1.5l-2.5-2-1.5 1.3c-1.5-.6-2.8-2-3.4-3.4L6.4 5.4 4.5 2.5z" fill="#fff"/></svg>021 555 01234</div>
      <div class="row"><svg viewBox="0 0 14 14"><rect x="1" y="4" width="12" height="8" fill="#fff"/><rect x="4" y="1" width="6" height="4" fill="#fff"/></svg>021 555 01234</div>
      <div class="row"><svg viewBox="0 0 14 14"><rect x="1" y="3" width="12" height="9" fill="#fff"/><path d="M1 3l6 5 6-5" fill="none" stroke="#2b2b2b" stroke-width="1.2"/></svg>hello@brambleroofing.co.nz</div>
    </div>
    <div class="footer-col location-map">
      <h5>LOCATION MAP</h5><div class="rule" style="visibility:hidden"></div>
      <div class="map-box" role="img" aria-label="Street map showing the company location"></div>
    </div>
    <div class="cert-badge" role="img" aria-label="Trade certification badge">
      <svg width="76" height="76" viewBox="0 0 76 76"><circle cx="38" cy="38" r="34" fill="none" stroke="#1b1b1b" stroke-width="3"/><circle cx="38" cy="38" r="20" fill="#1b1b1b"/></svg>
    </div>
  </div>
</footer>

<div class="bottom-bar">
  <div class="container">
    <div>Copyright © 2017 <strong>Bramble Roofing</strong>. All Rights Reserved</div>
    <svg width="36" height="36" viewBox="0 0 36 36" role="img" aria-label="Social page link"><rect x="8" y="8" width="20" height="20" transform="rotate(45 18 18)" fill="none" stroke="#fff" stroke-width="2"/><circle cx="18" cy="18" r="4" fill="#fff"/></svg>
  </div>
</div>

</body>
</html>
```